CRESTLINE Academy Exhibit Booth Posters

My company is CRESTLINE Academy (a division of CRESTLINE for Growth). We are exhibiting in a month, and I need to re-do my exhibit booth posters. There will be a total of 4 posters needed. Sizes are below.
1) Top- 11 feet long X 12 inches wide (Try to match color scheme in example photo)
2) Center- 4 feet long X 2 feet wide (Chalkboard background)
3) Left- 18 inches long X 2 feet wide (Cork-board back ground with the use of push pins holding up post-it-notes, paper, etc.)
4) Right- 18 inches long X 2 feet wide (Cork-board back ground with the use of push pins holding up post-it-notes, paper, etc.)
I have attached a photo of my old booth. This will get you an idea of the size, color schemes, and more. I have created basic rendering of each poster. The content is important, but the look and design should be drastically improved.
The websites to look into for ideas are:
www.crestlineforgrowth.example
www.crestlineacademy.example
Updates
I've added a new file. It's a .JPG of the certification diploma. Thanks!
Target Market(s)
Business Owners, Managers, HR, Supervisors, Teens who want to boost their resume
Industry/Entity Type
It Company
Look and feel

```html
<!DOCTYPE html>
<html lang="en">
<head>
<meta charset="utf-8">
<title>CRESTLINE Academy – Get your Employees Certified</title>
<link rel="stylesheet" href="https://fonts.googleapis.com/css2?family=Kalam:wght@400&family=UnifrakturMaguntia&family=Pinyon+Script&family=Libre+Baskerville:ital@0;1&display=swap">
<style>
  :root {
    --cork: #c8965a;
    --cork-light: #d6a86b;
    --cork-dark: #b07e44;
    --paper: #ffffff;
    --paper-shade: #e9e6e0;
    --ink-red: #d8231f;
    --pin-red: #c8191c;
    --note-yellow: #f7dc5a;
    --note-edge: #e6c43c;
    --gold: #c9a449;
    --gold-dark: #8a6a22;
    --cert-ink: #1d1d1d;
    --cert-paper: #fbfbf8;
    --photo-wall: #a9aab0;
    --photo-shirt: #1f2236;
  }
  * { margin: 0; padding: 0; box-sizing: border-box; }
  html, body { width: 900px; height: 1200px; overflow: hidden; }
  body {
    position: relative;
    background: radial-gradient(ellipse at 40% 40%, var(--cork-light), var(--cork) 55%, var(--cork-dark));
    font-family: "Kalam", cursive;
  }
  .poster { position: relative; width: 900px; height: 1200px; }
  .cork-board { position: absolute; inset: 0; }

  .torn-strip { position: absolute; }
  .torn-strip svg { display: block; }
  .strip-top { left: 50px; top: 14px; width: 790px; height: 340px; }
  .strip-bottom { left: 100px; top: 830px; width: 770px; height: 360px; }
  .strip-headline {
    position: absolute; left: 0; right: 0; text-align: center;
    color: var(--ink-red); font-family: "Kalam", cursive; font-weight: 400;
    line-height: 1;
  }
  .strip-top .line-one { top: 125px; font-size: 78px; }
  .strip-top .line-two { top: 218px; font-size: 80px; left: -20px; }
  .strip-bottom .line-one { top: 128px; font-size: 78px; }
  .strip-bottom .line-two { top: 222px; font-size: 80px; }

  .certificate {
    position: absolute; left: 40px; top: 385px; width: 630px; height: 460px;
    transform: rotate(-6deg);
    box-shadow: 4px 6px 10px rgba(0,0,0,.35);
  }
  .cert-frame {
    position: absolute; inset: 0;
    background: linear-gradient(135deg, #e9d38a, var(--gold) 40%, var(--gold-dark) 70%, #e3c977);
  }
  .cert-sheet {
    position: absolute; inset: 22px;
    background: var(--cert-paper);
    border: 2px solid var(--gold-dark);
    text-align: center; color: var(--cert-ink);
  }
  .cert-school { font-family: "UnifrakturMaguntia", cursive; font-size: 22px; margin-top: 22px; }
  .cert-title { font-family: "UnifrakturMaguntia", cursive; font-size: 27px; margin-top: 4px; }
  .cert-name {
    font-family: "Pinyon Script", cursive; font-size: 30px;
    width: 330px; margin: 8px auto 0; border-bottom: 1px solid var(--cert-ink); line-height: 1.2;
  }
  .cert-body {
    font-family: "Libre Baskerville", serif; font-size: 8.5px; line-height: 1.7;
    width: 520px; margin: 10px auto 0;
  }
  .cert-course { font-family: "UnifrakturMaguntia", cursive; font-size: 20px; margin: 4px 0 2px; }
  .cert-seal {
    position: absolute; left: 50%; top: 300px; width: 46px; height: 46px; margin-left: -23px;
    border-radius: 50%; background: radial-gradient(circle, #f3d25a, #2f6fc0 70%);
  }
  .cert-signature {
    position: absolute; left: 34px; bottom: 24px; width: 170px;
    border-top: 1px solid var(--cert-ink);
    font-family: "Libre Baskerville", serif; font-style: italic; font-size: 9px; text-align: left; padding-top: 2px;
  }
  .cert-date {
    position: absolute; right: 26px; top: 342px; width: 170px;
    border-top: 1px solid var(--cert-ink);
    font-family: "Libre Baskerville", serif; font-size: 10px; text-align: left; padding-top: 2px;
  }

  .sticky-note {
    position: absolute; width: 305px; height: 290px;
    background: linear-gradient(160deg, var(--note-yellow), var(--note-edge));
    box-shadow: 3px 5px 9px rgba(0,0,0,.35);
  }
  .note-before { left: 558px; top: 308px; transform: rotate(5deg); }
  .note-after { left: 556px; top: 640px; transform: rotate(-4deg); }
  .note-photo {
    position: absolute; left: 28px; top: 28px; width: 250px; height: 215px;
    background: linear-gradient(180deg, var(--photo-wall) 0 55%, var(--photo-shirt) 55%);
  }
  .note-caption {
    position: absolute; right: 34px; bottom: 4px;
    font-family: "Kalam", cursive; font-size: 22px; color: #2a2a2a;
  }

  .push-pin {
    position: absolute; width: 34px; height: 34px; border-radius: 50%;
    background: radial-gradient(circle at 35% 35%, #ff6a5e, var(--pin-red) 60%, #7d0c0d);
    box-shadow: 2px 3px 4px rgba(0,0,0,.4);
  }
</style>
</head>
<body>
<main class="poster">
  <div class="cork-board" role="img" aria-label="Cork board texture background"></div>

  <section class="torn-strip strip-top">
    <svg width="790" height="340" viewBox="0 0 790 340" aria-hidden="true">
      <polygon fill="var(--paper)" points="0,0 790,0 790,290 760,300 730,286 700,298 668,288 640,304 610,292 580,306 548,294 520,308 488,296 458,312 424,300 396,316 362,304 330,318 296,306 266,320 232,308 200,322 168,310 136,324 104,312 72,326 40,314 0,330"/>
      <g fill="var(--cork)">
        <circle cx="30" cy="44" r="11"/><circle cx="68" cy="44" r="11"/><circle cx="106" cy="44" r="11"/>
        <circle cx="144" cy="44" r="11"/><circle cx="182" cy="44" r="11"/><circle cx="220" cy="44" r="11"/>
        <circle cx="258" cy="44" r="11"/><circle cx="296" cy="44" r="11"/><circle cx="334" cy="44" r="11"/>
        <circle cx="372" cy="44" r="11"/><circle cx="410" cy="44" r="11"/><circle cx="448" cy="44" r="11"/>
        <circle cx="486" cy="44" r="11"/><circle cx="524" cy="44" r="11"/><circle cx="562" cy="44" r="11"/>
        <circle cx="600" cy="44" r="11"/><circle cx="638" cy="44" r="11"/><circle cx="676" cy="44" r="11"/>
        <circle cx="714" cy="44" r="11"/><circle cx="752" cy="44" r="11"/>
      </g>
    </svg>
    <h1 class="strip-headline line-one">Get your</h1>
    <h1 class="strip-headline line-two">Employees Certified</h1>
  </section>

  <section class="torn-strip strip-bottom">
    <svg width="770" height="360" viewBox="0 0 770 360" aria-hidden="true">
      <polygon fill="var(--paper)" points="0,24 30,14 62,28 96,12 128,26 160,10 194,24 228,8 262,22 296,6 330,20 364,4 398,18 432,2 466,16 500,0 534,14 568,2 602,16 636,4 670,18 704,6 738,18 770,8 770,350 0,360"/>
      <g fill="var(--cork)">
        <circle cx="30" cy="60" r="11"/><circle cx="68" cy="60" r="11"/><circle cx="106" cy="60" r="11"/>
        <circle cx="144" cy="60" r="11"/><circle cx="182" cy="60" r="11"/><circle cx="220" cy="60" r="11"/>
        <circle cx="258" cy="60" r="11"/><circle cx="296" cy="60" r="11"/><circle cx="334" cy="60" r="11"/>
        <circle cx="372" cy="60" r="11"/><circle cx="410" cy="60" r="11"/><circle cx="448" cy="60" r="11"/>
        <circle cx="486" cy="60" r="11"/><circle cx="524" cy="60" r="11"/><circle cx="562" cy="60" r="11"/>
        <circle cx="600" cy="60" r="11"/><circle cx="638" cy="60" r="11"/><circle cx="676" cy="60" r="11"/>
        <circle cx="714" cy="60" r="11"/><circle cx="752" cy="60" r="11"/>
      </g>
    </svg>
    <h2 class="strip-headline line-one">At a Price You</h2>
    <h2 class="strip-headline line-two">Cannot Pass Up!</h2>
  </section>

  <article class="certificate">
    <div class="cert-frame" role="img" aria-label="Ornamental gold certificate border"></div>
    <div class="cert-sheet">
      <p class="cert-school">CRESTLINE Academy</p>
      <p class="cert-title">Graduation Certification</p>
      <p class="cert-name">John Parker Doe</p>
      <p class="cert-body">This document certifies that the student named above has successfully graduated the CRESTLINE Academy</p>
      <p class="cert-course">Success At Work</p>
      <p class="cert-body">Interactive Training Certification Course with 100% passing score and has earned the title CRESTLINE Academy Graduate with all the rights and privileges thereunto appertaining. In witness thereof this Graduation Certificate is awarded by the facility at www.crestlineacademy.example upon the recommendation of the CRESTLINE Academy teaching staff as a direct result of this student's academic performance.</p>
      <div class="cert-seal" aria-hidden="true"></div>
      <p class="cert-date">Date of Graduation</p>
      <p class="cert-signature">CRESTLINE Academy Professor</p>
    </div>
  </article>

  <figure class="sticky-note note-before">
    <div class="note-photo" role="img" aria-label="Photo of an employee before certification, casually styled"></div>
    <figcaption class="note-caption">Before</figcaption>
  </figure>
  <figure class="sticky-note note-after">
    <div class="note-photo" role="img" aria-label="Photo of the same employee after certification, neatly groomed with ID badge"></div>
    <figcaption class="note-caption">After</figcaption>
  </figure>

  <span class="push-pin" role="img" aria-label="Push pin" style="left:100px;top:86px"></span>
  <span class="push-pin" role="img" aria-label="Push pin" style="left:796px;top:164px"></span>
  <span class="push-pin" role="img" aria-label="Push pin" style="left:322px;top:400px"></span>
  <span class="push-pin" role="img" aria-label="Push pin" style="left:740px;top:322px"></span>
  <span class="push-pin" role="img" aria-label="Push pin" style="left:662px;top:636px"></span>
  <span class="push-pin" role="img" aria-label="Push pin" style="left:108px;top:900px"></span>
  <span class="push-pin" role="img" aria-label="Push pin" style="left:790px;top:1018px"></span>
</main>
</body>
</html>
```